Plakate für Charity Unternehmen
Zielgruppe
Orek ist ein weltweit agierendes Charity Unternehmen.
Aufgabenstellung
Wir benötigen ein 'Plakat' Design, mit dem Zweck dieses Design als Banner, Sticker oder als Schild an unseren Projekten anzubringen. Das Schild soll in zwei verschiedenen Layouts geliefert werden.
1. Eine Art Blanko Version in der das Logo und das Motto eingearbeitet sind. Dieser Teil nimmt rund 1/3 des Plakats ein. Der Rest hat einen Freiraum auf dem wir Namen der Spender oder kooperative Charity Logos einsetzen können. Diese Version wird für Zusammenarbeit verwendet.
2. Eine zweite Version nimmt das gesamte Plakat ein, hier findet sich das Logo und das Motto welche das ganze Plakat einnehmen.
In beiden Fällen sollte die Aufteilung sauber und gut leserlich sein. Das Plakat wird in Auflösungen von bis zu 1,5m mal 1m gedruckt, sollte dementsprechend also die richtige Auflösung haben. Außerdem sollten Photoshop Datei möglichst mitgeliefert werden damit wir wenn nötig Namen und Logos einsetzen können.
Das einzuarbeitende Motto lautet:
إنما المؤمنون أخوة
Das Plakat sollte im Querformat sein und die Hintergrundfarbe sollte schwarz oder weiß sein.
Anbei befindet sich eine Beispieldatei wie das Plakat an den Projekten angebracht wird.

```html
<!DOCTYPE html>
<html lang="de">
<head>
<meta charset="utf-8">
<title>Orek – Plakat</title>
<link rel="stylesheet" href="https://fonts.googleapis.com/css2?family=Cinzel:wght@500&family=Noto+Naskh+Arabic:wght@400&display=swap">
<style>
  :root {
    --ink: #0e0e0e;
    --gold: #d3ad66;
    --blue: #1b72b8;
    --red: #d2481f;
    --white: #ffffff;
  }
  html, body {
    margin: 0;
    padding: 0;
    width: 1200px;
    height: 848px;
    overflow: hidden;
    background: var(--ink);
  }
  .poster {
    position: relative;
    width: 1200px;
    height: 848px;
    background: var(--ink);
    overflow: hidden;
  }
  .stripe-set {
    position: absolute;
    top: 203px;
    width: 330px;
    height: 98px;
  }
  .stripe-set--left { left: 0; }
  .stripe-set--right { right: 0; width: 337px; }
  .stripe {
    position: absolute;
    left: 0;
    right: 0;
  }
  .stripe--gold { top: 0; height: 59px; background: var(--gold); }
  .stripe--blue { top: 72px; height: 8px; background: var(--blue); }
  .stripe--red { top: 83px; height: 15px; background: var(--red); }

  .brand {
    position: absolute;
    left: 0;
    right: 0;
    top: 48px;
    display: flex;
    flex-direction: column;
    align-items: center;
  }
  .brand__mark {
    width: 230px;
    height: 230px;
    border-radius: 50%;
    background: var(--gold);
    margin-top: 40px;
  }
  .brand__name {
    margin: 50px 0 0;
    font-family: "Cinzel", "Times New Roman", serif;
    font-weight: 500;
    font-size: 118px;
    line-height: 1;
    letter-spacing: 2px;
    color: var(--white);
  }

  .motto {
    position: absolute;
    left: 30px;
    right: 30px;
    top: 520px;
    margin: 0;
    font-family: "Noto Naskh Arabic", "Amiri", serif;
    font-size: 150px;
    line-height: 1.1;
    text-align: center;
    color: var(--gold);
    white-space: nowrap;
  }

  .base-band {
    position: absolute;
    left: 0;
    right: 0;
    top: 781px;
    bottom: 0;
    background: var(--gold);
  }
</style>
</head>
<body>
  <main class="poster">
    <div class="stripe-set stripe-set--left">
      <div class="stripe stripe--gold"></div>
      <div class="stripe stripe--blue"></div>
      <div class="stripe stripe--red"></div>
    </div>
    <div class="stripe-set stripe-set--right">
      <div class="stripe stripe--gold"></div>
      <div class="stripe stripe--blue"></div>
      <div class="stripe stripe--red"></div>
    </div>

    <header class="brand">
      <div class="brand__mark" aria-hidden="true"></div>
      <h1 class="brand__name">OREK</h1>
    </header>

    <p class="motto" lang="ar" dir="rtl">إنما المؤمنون أخوة</p>

    <div class="base-band"></div>
  </main>
</body>
</html>
```